Vortane Labs - Methylene Blue Product Packaging

Our brand is Vortane Labs. We are launching a new product that is Methylene Blue, you can see more about this product if you search on Brisko or Pelludo and you will see what it is. This will be for a 50ml bottle. Give me different options for packaging that is minimalist and clean for this brand that makes it look well made and make people want to buy. I've added examples of what the bottle shape will be and potential packaging shapes so you can make packaging on those based off of that.

```html
<!DOCTYPE html>
<html lang="en">
<head>
<meta charset="UTF-8">
<title>Vortane Labs – Methylene Blue Label</title>
<link href="https://fonts.googleapis.com/css2?family=Poppins:wght@300;400;500;600;800&display=swap" rel="stylesheet">
<style>
  :root {
    --page-bg: #f4f4f4;
    --label-black: #0c0c0c;
    --text-white: #ffffff;
    --accent-blue: #2f8cff;
  }
  html, body {
    margin: 0;
    padding: 0;
    width: 700px;
    height: 1200px;
    overflow: hidden;
    background: var(--page-bg);
  }
  .canvas {
    position: relative;
    width: 700px;
    height: 1200px;
  }
  .label {
    position: absolute;
    left: 50px;
    top: 72px;
    width: 600px;
    height: 1056px;
    background: var(--label-black);
    font-family: 'Poppins', sans-serif;
    color: var(--text-white);
  }
  .brand {
    position: absolute;
    right: 45px;
    top: 52px;
    text-align: right;
    line-height: 1;
  }
  .brand-name {
    font-size: 80px;
    font-weight: 600;
    letter-spacing: -1px;
    display: flex;
    align-items: center;
    gap: 14px;
    justify-content: flex-end;
  }
  .brand-dot {
    width: 16px;
    height: 16px;
    border-radius: 50%;
    background: var(--text-white);
  }
  .brand-sub {
    font-size: 44px;
    font-weight: 400;
    margin-top: 4px;
    margin-right: 98px;
  }
  .product-name {
    position: absolute;
    right: 47px;
    top: 348px;
    text-align: right;
    line-height: 1;
  }
  .product-name-top {
    font-size: 56px;
    font-weight: 800;
    letter-spacing: 0.5px;
  }
  .product-name-accent {
    font-size: 92px;
    font-weight: 300;
    color: var(--accent-blue);
    letter-spacing: 2px;
    margin-top: 6px;
  }
  .claim-rule {
    position: absolute;
    left: 0;
    top: 778px;
    width: 400px;
    height: 4px;
    background: var(--accent-blue);
  }
  .claim-text {
    position: absolute;
    right: 228px;
    top: 720px;
    text-align: right;
    font-size: 31px;
    font-weight: 500;
    line-height: 1;
  }
  .claim-text span {
    display: block;
  }
  .claim-text .claim-line-bottom {
    margin-top: 34px;
  }
  .strength-badge {
    position: absolute;
    left: 396px;
    top: 709px;
    width: 146px;
    height: 142px;
  }
</style>
</head>
<body>
  <div class="canvas">
    <div class="label">
      <div class="brand">
        <div class="brand-name"><span class="brand-dot"></span>Vortane</div>
        <div class="brand-sub">Labs</div>
      </div>

      <div class="product-name">
        <div class="product-name-top">Methylene</div>
        <div class="product-name-accent">BLUE</div>
      </div>

      <div class="claim-rule"></div>
      <div class="claim-text">
        <span class="claim-line-top">Improves brain</span>
        <span class="claim-line-bottom">performance</span>
      </div>

      <svg class="strength-badge" viewBox="0 0 146 142" aria-label="1% concentration">
        <polygon points="38,4 108,4 142,71 108,138 38,138 4,71"
                 fill="none" stroke="var(--accent-blue)" stroke-width="5"/>
        <text x="73" y="88" text-anchor="middle" fill="var(--text-white)"
              font-family="Poppins, sans-serif" font-weight="600" font-size="48">1%</text>
      </svg>
    </div>
  </div>
</body>
</html>
```